Professional Services/Construction Management (Millwork) Biz Cards

We've decided on a logo and have our color palette set, now we want to design some very professional looking cards that make a strong first impression - they'll reflect our tagline (that we're going to put on the back: Innovative. Professional. Leaders.

The example business card shows generally the direction we've been thinking of going for the back side - **but we're open to other ideas**

Target Market(s)

The cards should target more high-end (wealthy) owners and general contracting companies. We want them to convey a strong first impression - in a professional and not garish way.

Industry/Entity Type

Construction Company

Contact Information for Business Card

There needs to be a place for our company contractor's license number and business address. We want to also have people's names, titles, phone number, email address. The back can be the logo, tagline and web address

Requirements
Must have
• follow our color palette
Nice to have
• Font & Styles should compliment the Harrow Joinery fonts, but not necessarily match exactly

```html
<!DOCTYPE html>
<html lang="en">
<head>
<meta charset="utf-8">
<title>Harrow Joinery – Business Card</title>
<link rel="stylesheet" href="https://fonts.googleapis.com/css2?family=Open+Sans:wght@400;700&display=swap">
<style>
  :root {
    --backdrop: #e9e6e3;
    --card-white: #ffffff;
    --earth-brown: #5d4e42;
    --dusty-mauve: #a68b89;
    --leaf-green: #4f9a3d;
    --text-light: #ffffff;
  }
  * { margin: 0; padding: 0; box-sizing: border-box; }
  html, body {
    width: 1200px;
    height: 900px;
    overflow: hidden;
    background: var(--backdrop);
    font-family: "Open Sans", Arial, sans-serif;
  }
  .business-card {
    position: absolute;
    left: 150px;
    top: 172px;
    width: 900px;
    height: 556px;
    background: var(--card-white);
    overflow: hidden;
    box-shadow: 0 6px 24px rgba(0,0,0,0.15);
  }
  .card-waves {
    position: absolute;
    inset: 0;
    width: 100%;
    height: 100%;
  }
  .brand-mark {
    position: absolute;
    left: 106px;
    top: 139px;
    width: 242px;
    height: 242px;
    border-radius: 50%;
    background: var(--earth-brown);
  }
  .brand-name {
    position: absolute;
    left: 106px;
    top: 300px;
    width: 242px;
    text-align: center;
    font-weight: 700;
    font-size: 26px;
    line-height: 34px;
    color: var(--leaf-green);
  }
  .contact-line {
    position: absolute;
    right: 22px;
    color: var(--text-light);
    text-align: right;
    white-space: nowrap;
    font-size: 22px;
    line-height: 30px;
  }
  .person-name { top: 246px; font-size: 30px; line-height: 34px; font-weight: 700; }
  .person-title { top: 280px; font-size: 23px; }
  .address-line-1 { top: 334px; }
  .address-line-2 { top: 365px; }
  .contact-line.with-icon { right: 22px; display: flex; align-items: center; gap: 14px; }
  .phone-line { top: 422px; }
  .email-line { top: 454px; }
  .web-line { top: 485px; }
  .contact-icon { width: 17px; height: 17px; fill: var(--text-light); flex: none; }
</style>
</head>
<body>
  <div class="business-card">
    <svg class="card-waves" viewBox="0 0 653 403" preserveAspectRatio="none" aria-hidden="true">
      <path fill="var(--dusty-mauve)" d="M0,206 C70,293 180,316 290,266 C390,220 490,116 580,118 C620,119 645,138 653,150 L653,163 C645,151 620,134 580,133 C490,132 390,234 290,280 C180,328 70,306 0,222 Z"/>
      <path fill="var(--earth-brown)" d="M0,232 C70,316 180,338 290,290 C390,246 490,146 580,146 C620,146 645,160 653,172 L653,403 L0,403 Z"/>
    </svg>

    <div class="brand-mark"></div>
    <div class="brand-name">Harrow Joinery</div>

    <div class="contact-line person-name">Daniel Hale</div>
    <div class="contact-line person-title">Managing Director</div>
    <div class="contact-line address-line-1">12345, Address Goes Here</div>
    <div class="contact-line address-line-2">Country Name, 123456.</div>

    <div class="contact-line with-icon phone-line">
      <span>044-555 010 274</span>
      <svg class="contact-icon" viewBox="0 0 24 24" aria-hidden="true"><path d="M6.6 10.8a15.1 15.1 0 0 0 6.6 6.6l2.2-2.2a1 1 0 0 1 1-.25 11.4 11.4 0 0 0 3.6.57 1 1 0 0 1 1 1V20a1 1 0 0 1-1 1A17 17 0 0 1 3 4a1 1 0 0 1 1-1h3.5a1 1 0 0 1 1 1c0 1.25.2 2.45.57 3.57a1 1 0 0 1-.25 1z"/></svg>
    </div>
    <div class="contact-line with-icon email-line">
      <span>info@harrowjoinery.com</span>
      <svg class="contact-icon" viewBox="0 0 24 24" aria-hidden="true"><path d="M2 5h20v14H2z M2 5l10 8 10-8" fill="var(--text-light)" stroke="var(--earth-brown)" stroke-width="1.6"/></svg>
    </div>
    <div class="contact-line with-icon web-line">
      <span>www.harrowjoinery.com</span>
      <svg class="contact-icon" viewBox="0 0 24 24" aria-hidden="true"><circle cx="12" cy="12" r="10"/><path d="M2 12h20M12 2c3 3 3 17 0 20M12 2c-3 3-3 17 0 20M4 7h16M4 17h16" fill="none" stroke="var(--earth-brown)" stroke-width="1.4"/></svg>
    </div>
  </div>
</body>
</html>
```